Quillmere business card

We're looking to "refresh" our original Quillmere logo design and also get a new business card design. We're a modern consulting and software business that's been around 4-years now. We work with large professional companies and therefore require a design that is simple and professional. We would like to retain the notch in the "A" and just the word "Quillmere" as the logo. We like greys, silvers, black, white...but happy to explore highlight color. We're looking for understated modern.

Industry/Entity Type

Software

```html
<!DOCTYPE html>
<html lang="en">
<head>
<meta charset="utf-8">
<title>Quillmere Business Card</title>
<link href="https://fonts.googleapis.com/css2?family=Lato:wght@400;700;900&display=swap" rel="stylesheet">
<style>
  :root {
    --bg: #d9d9d6;
    --card-dark: #141414;
    --card-mid: #2b2b2b;
    --teal: #14a89c;
    --teal-light: #1cbcae;
    --teal-deep: #0f8d83;
    --white: #ffffff;
    --soft-white: #e9e9e9;
  }
  * { margin: 0; padding: 0; box-sizing: border-box; }
  html, body {
    width: 1200px;
    height: 1000px;
    overflow: hidden;
    background: var(--bg);
    font-family: "Lato", Arial, sans-serif;
  }
  .canvas {
    position: relative;
    width: 1200px;
    height: 1000px;
  }
  .card {
    position: absolute;
    left: 220px;
    width: 760px;
    height: 434px;
    overflow: hidden;
    background: radial-gradient(ellipse at 55% 40%, var(--card-mid) 0%, var(--card-dark) 75%);
    box-shadow: 0 10px 24px rgba(0,0,0,0.25);
  }
  .card--back { top: 44px; }
  .card--front { top: 522px; }
  .card-folds {
    position: absolute;
    inset: 0;
    width: 100%;
    height: 100%;
  }
  .wordmark {
    position: absolute;
    font-family: "Lato", Arial, sans-serif;
    font-weight: 900;
    color: var(--white);
    text-transform: uppercase;
    letter-spacing: 2px;
    line-height: 1;
  }
  .card--back .wordmark {
    left: 340px;
    top: 150px;
    font-size: 68px;
  }
  .website {
    position: absolute;
    left: 344px;
    top: 238px;
    font-size: 22px;
    letter-spacing: 5px;
    color: var(--teal);
  }
  .card--front .wordmark {
    left: 56px;
    top: 52px;
    font-size: 60px;
  }
  .identity {
    position: absolute;
    left: 58px;
    top: 140px;
  }
  .identity__name {
    font-size: 26px;
    color: var(--white);
    letter-spacing: 0.5px;
  }
  .identity__title {
    font-size: 20px;
    color: var(--teal);
    margin-top: 4px;
  }
  .contact {
    position: absolute;
    left: 58px;
    top: 240px;
    list-style: none;
    font-size: 18px;
    line-height: 30px;
    color: var(--soft-white);
  }
  .contact__label { color: var(--teal); }
</style>
</head>
<body>
<main class="canvas">

  <section class="card card--back" aria-label="Card back">
    <svg class="card-folds" viewBox="0 0 760 434" aria-hidden="true">
      <polygon points="0,0 300,0 0,300" fill="var(--teal)"/>
      <polygon points="0,0 250,0 0,360" fill="var(--teal-light)"/>
      <polygon points="0,0 190,0 0,410" fill="var(--teal)"/>
      <polygon points="0,0 120,0 0,434" fill="var(--teal-deep)"/>
      <polygon points="760,434 620,434 760,330" fill="var(--teal)"/>
    </svg>
    <div class="wordmark">Quillmere</div>
    <div class="website">www.quillmere.com.au</div>
  </section>

  <section class="card card--front" aria-label="Card front">
    <svg class="card-folds" viewBox="0 0 760 434" aria-hidden="true">
      <polygon points="760,434 480,434 760,300" fill="var(--teal)"/>
      <polygon points="760,434 580,434 760,340" fill="var(--teal-light)"/>
      <polygon points="760,0 660,0 760,70" fill="var(--teal)"/>
    </svg>
    <div class="wordmark">Quillmere</div>
    <div class="identity">
      <div class="identity__name">YOUR NAME</div>
      <div class="identity__title">Title</div>
    </div>
    <ul class="contact">
      <li><span class="contact__label">Phone:</span> 123 456 7890</li>
      <li><span class="contact__label">Mobile:</span> 123 456 7890</li>
      <li><span class="contact__label">Email:</span> yourname@quillmere.com</li>
      <li><span class="contact__label">Address:</span> St. 1, Harlow Lane, Brookfield, NY 123345</li>
    </ul>
  </section>

</main>
</body>
</html>
```